Meleku Presents: Pelawi's Reef Echoes

I need to create a flyer for a concert on June 14, 2024
Doors Open at 8pm - 12am

Band 1 : The Lads Of Sundrift : Tevaru / Pilesu https://www.snapgallery.example/p/XQt7Lm2RzP4/?hl=en&img_index=1
& FEATURING: Merio https://www.snapgallery.example/merotunes_audio/?hl=en

Band 2: Low Tydez
https://www.filecrate.example/scl/fo/qwpz81mnbv47tyrcx02kd/BXnePL5QwRT9HKz3MdVmtuy?rlkey=7hqz112ksmwp38ytnbvaxc5d1&dl=0

Band 3: Danny Corvel
https://www.filecrate.example/scl/fo/k2ptm8rqzd61bhxwnya4e/h?rlkey=zb3mnq71trc52xqplgdje8f0k&dl=0

Kaua'i located at the Marlow Terrace Lodge at Pinecrest Cove
( 7-2184 Nalemo Rd Pukoli HI 96812)

I will need a couple variations of the flyer design per designer.

Also With your flyer id like you to formulate a TICKET that has the same theme as your flyer design. On the side of the ticket will need to be perforated to separate and numbered.

i need to change the artists and all info on the event as it has been pushed back a month

Target Market(s)

21 and over Event

Requirements
Must have
• Listed on Flyer Only: DRESS CODE: Collard Shirts for Men is required
Nice to have
• These two: Danny Corvel Main Artist - Low Tydez Second Artist to Showcase

```html
<!DOCTYPE html>
<html lang="en">
<head>
<meta charset="utf-8">
<title>Meleku Presents – Pelawi's Reef Echoes</title>
<link rel="stylesheet" href="https://fonts.googleapis.com/css2?family=Almendra:wght@400;700&family=Montserrat:wght@500;600;700&display=swap">
<style>
  :root {
    --night: #1c2a6b;
    --midnight: #141a45;
    --violet: #4a3a8a;
    --dusk: #8a3f7e;
    --sunset: #c4577e;
    --shore: #2a1634;
    --ring: #e040f0;
    --ring-glow: rgba(224, 64, 240, 0.7);
    --ink: #ffffff;
  }
  * { box-sizing: border-box; }
  html, body {
    margin: 0;
    width: 845px;
    height: 1200px;
    overflow: hidden;
    background: var(--midnight);
  }
  .flyer {
    position: relative;
    width: 845px;
    height: 1200px;
    overflow: hidden;
    color: var(--ink);
    font-family: "Montserrat", Arial, sans-serif;
  }
  .backdrop {
    position: absolute;
    inset: 0;
    background:
      radial-gradient(ellipse 70% 30% at 50% 72%, rgba(196, 87, 126, 0.75), transparent 70%),
      linear-gradient(180deg, var(--midnight) 0%, var(--night) 25%, var(--violet) 50%, var(--dusk) 66%, var(--sunset) 76%, var(--shore) 88%, #1a0f24 100%);
  }
  .presenter {
    position: absolute;
    top: 36px;
    left: 0;
    width: 100%;
    text-align: center;
    font-weight: 700;
    font-size: 30px;
    letter-spacing: 7px;
  }
  .event-title {
    position: absolute;
    top: 94px;
    left: 0;
    width: 100%;
    margin: 0;
    text-align: center;
    font-family: "Almendra", Georgia, serif;
    font-weight: 700;
    font-size: 84px;
    line-height: 1;
  }
  .event-date {
    position: absolute;
    top: 208px;
    left: 0;
    width: 100%;
    text-align: center;
    font-family: "Almendra", Georgia, serif;
    font-weight: 700;
    font-size: 66px;
    line-height: 1;
  }
  .artist {
    position: absolute;
    width: 270px;
    text-align: center;
  }
  .artist-photo {
    width: 240px;
    height: 240px;
    margin: 0 auto;
    border-radius: 50%;
    border: 4px solid var(--ring);
    box-shadow: 0 0 14px var(--ring-glow), inset 0 0 12px var(--ring-glow);
    background: radial-gradient(circle at 50% 40%, #8a6a5c 0%, #4a3a4a 55%, #2a2440 100%);
  }
  .artist-name {
    margin-top: 12px;
    font-family: "Almendra", Georgia, serif;
    font-weight: 700;
    font-size: 34px;
    line-height: 1;
  }
  .artist-name.stacked { font-size: 27px; line-height: 1.08; }
  .artist.headliner { left: 30px; top: 330px; }
  .artist.second { left: 287px; top: 330px; }
  .artist.group { left: 552px; top: 330px; }
  .artist.dj { left: 287px; top: 648px; }
  .time-block {
    position: absolute;
    top: 712px;
    width: 250px;
    text-align: center;
  }
  .time-block.doors { left: 30px; }
  .time-block.show { left: 568px; }
  .time-label {
    font-weight: 600;
    font-size: 28px;
    letter-spacing: 0.5px;
  }
  .time-value {
    margin-top: 14px;
    font-family: "Almendra", Georgia, serif;
    font-weight: 700;
    font-size: 76px;
    line-height: 1;
  }
  .time-value sup {
    font-size: 40px;
    vertical-align: 26px;
  }
  .divider {
    position: absolute;
    top: 966px;
    left: 36px;
    width: 774px;
    height: 2px;
    background: var(--ink);
  }
  .details {
    position: absolute;
    top: 990px;
    left: 0;
    width: 100%;
    text-align: center;
    font-weight: 600;
    font-size: 21px;
    line-height: 1;
  }
  .details p { margin: 0 0 11px; }
  .details .address {
    font-size: 15px;
    margin-top: -6px;
    margin-bottom: 13px;
  }
  .details .after-party { margin-bottom: 6px; }
  .details .after-address { font-size: 21px; }
  .details .after-address small { font-size: 15px; }
</style>
</head>
<body>
<main class="flyer">
  <div class="backdrop" role="img" aria-label="Night sky full of stars over a tropical beach at sunset, framed by silhouetted palm trees"></div>

  <div class="presenter">MELEKU PRESENTS</div>
  <h1 class="event-title">Pelawi's Reef Echoes</h1>
  <div class="event-date">June 14, 2024</div>

  <section class="artist headliner">
    <div class="artist-photo" role="img" aria-label="Portrait photo of Danny Corvel"></div>
    <div class="artist-name">Danny Corvel</div>
  </section>
  <section class="artist second">
    <div class="artist-photo" role="img" aria-label="Photo of the duo Low Tydez"></div>
    <div class="artist-name">Low Tydez</div>
  </section>
  <section class="artist group">
    <div class="artist-photo" role="img" aria-label="Group photo of The Lads Of Sundrift with Merio"></div>
    <div class="artist-name stacked">The Lads Of Sundrift<br>Tevaru &amp; Pilesu<br>with Merio</div>
  </section>

  <div class="time-block doors">
    <div class="time-label">DOORS OPEN</div>
    <div class="time-value">8<sup>pm</sup></div>
  </div>

  <section class="artist dj">
    <div class="artist-photo" role="img" aria-label="Portrait photo of DJ Vexon"></div>
    <div class="artist-name">DJ Vexon</div>
  </section>

  <div class="time-block show">
    <div class="time-label">SHOW ENDS</div>
    <div class="time-value">12<sup>am</sup></div>
  </div>

  <div class="divider"></div>

  <section class="details">
    <p>TICKETED EVENT: 21 and over</p>
    <p>DRESS CODE:&nbsp; Collared Shirt for all Men required</p>
    <p>LOCATION: Marlow Terrace Lodge at Pinecrest Cove</p>
    <p class="address">(7-2184 Nalemo Rd Pukoli HI 96812)</p>
    <p class="after-party">AFTER PARTY: Hosted By Tokaru Grill's at Palmview Commons</p>
    <p class="after-address"><small>(9-317 Halrena Rd Pukoli HI 96812)</small> with DJ Vexon</p>
  </section>
</main>
</body>
</html>
```